FUN Construction Open House Invitation

Open House for New Office of LVDP Construction, we have a logo, not sure what other graphics to put on the invitation and make it fun

Main target audience: Residential Building Architects (Custom Homes)
so we want to maybe target it towards that with a sketch of design/house/plans?
Drinks and food at: Mellow Burrito around the corner
LUCKY DOOR PRIZES: zobex, etc (need to be present to win)
Current BORING design attached
Event is on Thursday, 7/15 from 3-6 pm
Location: 518 Kelmont Row, Suite 307-2 in Laguna Beach
Company: LVDP Construction (logo attached)
RSVP by 7/12 to office@lvdp.construction or 949-555-0173

Target Market(s)

Residential Building Architects for Custom Homes

Font styles to use
Other font styles liked:
• SOMETHING MODERN

Requirements
Must have
• Graphics, MODERN & FUN & ARTSY look but not too crowded
Should it be a charicature of the team? (with our english bulldog?)
A charicature of our english bulldog on a surfboard or skateboard or too cheesy?
Should not have
• Hammer or any other graphics like that, we are not a handyman company
High end custom home construction working with architects

```html
<!DOCTYPE html>
<html lang="en">
<head>
<meta charset="utf-8">
<title>LVDP Construction Open House Invitation</title>
<link href="https://fonts.googleapis.com/css2?family=Montserrat:wght@500;600;700;800&family=Oswald:wght@500;600;700&display=swap" rel="stylesheet">
<style>
  :root {
    --orange: #ef7a33;
    --charcoal: #333335;
    --grey: #7a7a7c;
    --paper: #ffffff;
    --backdrop: #e4e4e4;
    --sky: #8fa6da;
    --wall: #c8b8a6;
    --glow: #e9c98f;
    --water: #55504c;
  }
  * { margin: 0; padding: 0; box-sizing: border-box; }
  html, body { width: 1200px; height: 1200px; overflow: hidden; }
  body { background: var(--backdrop); position: relative; font-family: "Montserrat", sans-serif; color: var(--charcoal); }

  .invitation {
    position: absolute; left: 40px; top: 249px;
    width: 1120px; height: 702px;
    background: var(--paper); overflow: hidden;
  }

  .house-render {
    position: absolute; inset: 0;
    clip-path: polygon(628px 0, 1120px 0, 1120px 702px, 481px 702px);
    background:
      linear-gradient(180deg, rgba(143,166,218,0.95) 0%, rgba(190,196,220,0.7) 18%, rgba(200,184,166,0.2) 35%),
      radial-gradient(ellipse at 62% 62%, var(--glow) 0%, rgba(233,201,143,0) 38%),
      linear-gradient(180deg, var(--sky) 0%, #c9c3c6 25%, var(--wall) 50%, #b6a595 75%, var(--water) 100%);
  }

  .brand { position: absolute; left: 0; width: 568px; top: 44px; text-align: center; }
  .brand-name {
    display: inline-flex; align-items: center; gap: 12px;
    font-family: "Montserrat", sans-serif; font-weight: 800; color: var(--orange);
    font-size: 46px; line-height: 1; letter-spacing: 1px;
  }
  .brand-mark { width: 30px; height: 30px; background: var(--orange); }
  .brand-sub {
    font-weight: 800; color: var(--orange); font-size: 24px; letter-spacing: 1.5px; margin-top: 4px;
  }
  .brand-web { font-weight: 600; color: var(--grey); font-size: 13px; margin-top: 2px; letter-spacing: 0.3px; }

  .banner-food {
    position: absolute; left: 33px; top: 177px; width: 501px; height: 50px;
    background: var(--orange);
    clip-path: polygon(24px 0, 100% 0, calc(100% - 20px) 100%, 0 100%);
    color: #fff; font-weight: 800; font-size: 32px;
    display: flex; align-items: center; justify-content: center; letter-spacing: 0.3px;
  }
  .banner-venue {
    position: absolute; left: 58px; top: 228px; width: 429px; height: 46px;
    background: var(--charcoal);
    clip-path: polygon(22px 0, 100% 0, calc(100% - 20px) 100%, 0 100%);
    color: #fff; font-weight: 500; font-size: 22px;
    display: flex; align-items: center; justify-content: center;
  }

  .prizes-title {
    position: absolute; left: 40px; top: 298px;
    display: flex; align-items: center; gap: 8px;
    font-family: "Oswald", sans-serif; font-weight: 700; color: var(--orange);
    font-size: 46px; line-height: 1;
  }
  .prizes-icon { width: 34px; height: 38px; }
  .prizes-note {
    position: absolute; left: 93px; top: 358px;
    font-size: 19px; font-weight: 500; color: var(--charcoal);
  }
  .prizes-note strong { color: var(--orange); font-weight: 700; }

  .ticket { position: absolute; left: 63px; top: 405px; width: 396px; height: 166px; display: flex; }
  .ticket-tab {
    width: 55px; background: var(--charcoal);
    display: flex; align-items: center; justify-content: center;
    border: 3px dotted #fff; border-right: none;
  }
  .ticket-tab span {
    transform: rotate(-90deg); white-space: nowrap;
    font-family: "Oswald", sans-serif; font-weight: 600; color: #fff; font-size: 27px; letter-spacing: 0.5px;
  }
  .ticket-body {
    flex: 1; background: var(--orange); border: 3px dotted #fff; border-left: none;
    display: flex; flex-direction: column; align-items: center; padding-top: 20px; color: #fff;
  }
  .ticket-date {
    display: flex; align-items: center; gap: 8px;
    font-family: "Oswald", sans-serif; font-weight: 500; font-size: 26px; line-height: 1;
  }
  .ticket-time {
    margin-top: 12px; width: 196px; height: 36px; background: var(--charcoal);
    clip-path: polygon(0 0, 100% 0, calc(100% - 10px) 50%, 100% 100%, 0 100%, 10px 50%);
    display: flex; align-items: center; justify-content: center; gap: 8px;
    font-family: "Oswald", sans-serif; font-weight: 500; font-size: 24px;
  }
  .ticket-place {
    margin-top: 12px; text-align: center; font-weight: 700; font-size: 14px; line-height: 22px;
  }
  .ticket-place svg { vertical-align: -2px; margin-right: 4px; }

  .rsvp {
    position: absolute; left: 40px; top: 594px; width: 414px;
    display: flex; align-items: center; gap: 10px;
    font-family: "Oswald", sans-serif; font-weight: 500; font-size: 20px; white-space: nowrap;
  }
  .rsvp::before, .rsvp::after { content: ""; flex: 1; height: 1.5px; background: var(--orange); }
  .rsvp-label { color: var(--orange); }
  .rsvp-date { color: var(--charcoal); }

  .contact-pill {
    position: absolute; left: 26px; top: 639px; width: 429px; height: 36px;
    border: 1.5px solid var(--charcoal); border-radius: 18px;
    display: flex; align-items: center; justify-content: space-around; padding: 0 8px;
    font-weight: 600; font-size: 16px;
  }
  .contact-item { display: flex; align-items: center; gap: 6px; }
  .contact-item .accent { color: var(--orange); }
  .contact-icon { width: 22px; height: 22px; border-radius: 50%; background: var(--orange); display: flex; align-items: center; justify-content: center; }
</style>
</head>
<body>
  <main class="invitation">
    <div class="house-render" role="img" aria-label="Photo of a modern two-storey custom home at dusk with glowing windows and a reflecting pool, overlaid with an architectural wireframe sketch and handwritten dimension notes"></div>

    <header class="brand">
      <div class="brand-name"><span class="brand-mark"></span>LVDP</div>
      <div class="brand-sub">CONSTRUCTION</div>
      <div class="brand-web">www.lvdp.construction</div>
    </header>

    <div class="banner-food">DRINKS AND FOOD AT:</div>
    <div class="banner-venue">Mellow Burrito around the corner</div>

    <div class="prizes-title">
      <svg class="prizes-icon" viewBox="0 0 34 38" aria-hidden="true">
        <rect x="3" y="8" width="28" height="28" rx="4" fill="#fff" stroke="#333335" stroke-width="2"/>
        <rect x="7" y="12" width="20" height="20" rx="2" fill="#ef7a33"/>
        <path d="M17 8 L12 2 M17 8 L22 2" stroke="#ef7a33" stroke-width="2" fill="none"/>
      </svg>
      LUCKY DOOR PRIZES:
    </div>
    <p class="prizes-note"><strong>zobex,</strong> etc (need to be present to win)</p>

    <section class="ticket">
      <div class="ticket-tab"><span>EVENT IS ON</span></div>
      <div class="ticket-body">
        <div class="ticket-date">
          <svg width="22" height="22" viewBox="0 0 22 22" aria-hidden="true">
            <rect x="2" y="4" width="18" height="16" rx="2" fill="none" stroke="#fff" stroke-width="1.8"/>
            <line x1="2" y1="9" x2="20" y2="9" stroke="#fff" stroke-width="1.8"/>
            <line x1="7" y1="2" x2="7" y2="6" stroke="#fff" stroke-width="1.8"/>
            <line x1="15" y1="2" x2="15" y2="6" stroke="#fff" stroke-width="1.8"/>
          </svg>
          THURSDAY, 15TH JULY, 2021
        </div>
        <div class="ticket-time">
          <svg width="20" height="20" viewBox="0 0 20 20" aria-hidden="true">
            <circle cx="10" cy="10" r="8" fill="none" stroke="#fff" stroke-width="1.8"/>
            <path d="M10 5 V10 L13 12" stroke="#fff" stroke-width="1.8" fill="none"/>
          </svg>
          FROM 3-6 PM
        </div>
        <div class="ticket-place">
          <svg width="12" height="14" viewBox="0 0 12 14" aria-hidden="true">
            <path d="M6 0 C2.7 0 0 2.6 0 5.8 C0 10 6 14 6 14 C6 14 12 10 12 5.8 C12 2.6 9.3 0 6 0 Z" fill="#fff"/>
            <circle cx="6" cy="5.8" r="2.2" fill="#ef7a33"/>
          </svg>518 Kelmont Row,<br>Suite 307-2 in Laguna Beach
        </div>
      </div>
    </section>

    <div class="rsvp"><span class="rsvp-label">RSVP BY:</span><span class="rsvp-date">12 JULY, TO</span></div>

    <div class="contact-pill">
      <div class="contact-item">
        <span class="contact-icon">
          <svg width="12" height="10" viewBox="0 0 12 10" aria-hidden="true">
            <rect x="0.5" y="0.5" width="11" height="9" rx="1" fill="none" stroke="#fff"/>
            <path d="M0.5 1 L6 5.5 L11.5 1" fill="none" stroke="#fff"/>
          </svg>
        </span>
        <span>office@<span class="accent">lvdp.construction</span></span>
      </div>
      <div class="contact-item">
        <span class="contact-icon">
          <svg width="12" height="12" viewBox="0 0 24 24" aria-hidden="true">
            <path d="M6.6 10.8a15.1 15.1 0 0 0 6.6 6.6l2.2-2.2a1 1 0 0 1 1-.25 11.4 11.4 0 0 0 3.6.57 1 1 0 0 1 1 1V20a1 1 0 0 1-1 1A17 17 0 0 1 3 4a1 1 0 0 1 1-1h3.5a1 1 0 0 1 1 1c0 1.25.2 2.46.57 3.6a1 1 0 0 1-.25 1z" fill="#fff"/>
          </svg>
        </span>
        <span>949-555-0173</span>
      </div>
    </div>
  </main>
</body>
</html>
```